website name will be called www.nextridgepower.com
Please us color red, white,grey if possible
We are a solar provider that will offer solar ownership and leases with 25yr warranty and labor. Over 20yrs combined solar experience

Number of Pages Required

1 page

```html
<!DOCTYPE html>
<html lang="en">
<head>
<meta charset="utf-8">
<title>NextRidge Power – Solar Ownership &amp; Leases</title>
<link href="https://fonts.googleapis.com/css2?family=Roboto:ital,wght@0,400;0,500;0,700;1,400&display=swap" rel="stylesheet">
<style>
:root{
  --red:#c4161c;
  --red-dark:#a5121a;
  --red-band:#b3242b;
  --white:#ffffff;
  --ink:#111111;
  --grey:#6b6b6b;
  --grey-light:#e9e9e9;
  --line:#d5d5d5;
  --footer:#0b0b0b;
}
*{box-sizing:border-box;margin:0;padding:0}
html,body{width:1200px;height:5343px;overflow:hidden}
body{position:relative;font-family:"Roboto",Arial,sans-serif;color:var(--ink);background:var(--white)}
.abs{position:absolute}
.section-title{position:absolute;left:0;width:1200px;text-align:center;font-weight:700;font-size:36px;text-transform:uppercase;letter-spacing:.3px}
.btn{position:absolute;display:flex;align-items:center;justify-content:center;background:var(--red);color:var(--white);font-weight:700;font-size:15px;border-radius:24px;text-transform:uppercase}
.body-text{font-size:13px;line-height:28px;color:var(--grey)}

/* Header / hero */
.hero{position:absolute;left:0;top:0;width:1200px;height:616px;
  background:linear-gradient(180deg,#e4eaf0 0%,#cfd9e3 45%,#9fb0c4 62%,#3d5e96 78%,#213e79 100%)}
.brand{position:absolute;left:110px;top:60px;display:flex;align-items:center;gap:8px;font-size:28px;font-weight:700;color:#555}
.brand .dot{width:14px;height:14px;border-radius:50%;background:var(--red)}
.nav{position:absolute;top:34px;left:414px;display:flex;gap:48px;font-size:14px;font-weight:500;text-transform:uppercase}
.nav .active{color:var(--red);border-bottom:2px solid var(--red);padding-bottom:3px}
.quote-btn{left:934px;top:22px;width:154px;height:42px;font-size:14px}
.hero h1{position:absolute;left:108px;top:228px;font-size:84px;font-weight:700;line-height:1}
.hero p{position:absolute;left:114px;top:322px;font-size:15px;line-height:30px;color:#222}
.hero-btn{left:114px;top:393px;width:155px;height:42px}
.arrow{position:absolute;top:286px;width:18px;height:34px}
.dots{position:absolute;display:flex;gap:8px}
.dots span{width:11px;height:11px;border-radius:50%;background:var(--white);opacity:.8}
.dots.grey span{background:#cfcfcf}
.dots.grey span:first-child{background:var(--white)}

/* About */
.about-frame{left:110px;top:705px;width:456px;height:388px;background:var(--red)}
.about-photo{left:122px;top:712px;width:452px;height:389px;background:linear-gradient(150deg,#dfe5ee 0%,#8ea6cc 40%,#3b5d9b 100%)}
.about h2{position:absolute;left:657px;top:742px;font-size:36px;font-weight:700}
.about .body-text{position:absolute;left:655px;top:801px;width:432px;font-size:13.5px}
.about-btn{left:655px;top:1008px;width:155px;height:42px}

/* Spectrum */
.spectrum{position:absolute;left:0;top:1186px;width:1200px;height:508px;background:linear-gradient(135deg,#b2242c 0%,#a01820 100%)}
.spectrum .section-title{color:var(--white);top:60px;font-size:34px}
.service{position:absolute;top:139px;width:301px;height:299px;border:1px solid rgba(255,255,255,.6);border-radius:10px;color:var(--white);text-align:center}
.service svg{margin-top:34px}
.service h3{font-size:21px;font-weight:700;margin-top:14px}
.service p{font-size:12.5px;line-height:24px;margin:10px 14px 0;opacity:.95}

/* Why */
.why .section-title{top:1757px;font-size:34px}
.feature{position:absolute;width:270px;z-index:2}
.feature h4{font-size:21px;font-weight:700}
.feature p{font-size:14px;line-height:26px;color:var(--grey);margin-top:6px}
.feature.right{text-align:right}
.icon-circle{position:absolute;width:72px;height:72px;border-radius:50%;background:var(--red);border:4px solid #f1d0d2;display:flex;align-items:center;justify-content:center}
.why-art{left:420px;top:1850px;width:360px;height:365px;border-radius:48%;background:radial-gradient(circle at 50% 55%,#4a7bd1 0%,#8fb8e8 40%,#cfe8b8 66%,#ffffff 84%);z-index:1}

/* Testimonials */
.testimonials{position:absolute;left:0;top:2300px;width:1200px;height:473px;background:linear-gradient(135deg,#b3242b 0%,#c9353b 100%);color:var(--white)}
.testimonials .section-title{top:70px}
.quote{position:absolute;top:156px;width:400px}
.quote p{font-style:italic;font-size:14px;line-height:28px}
.quote h5{font-size:19px;font-weight:700;margin-top:14px}
.quote small{font-size:13px;display:block;margin-top:2px}
.avatar{position:absolute;top:152px;width:66px;height:66px;border-radius:50%;border:3px solid var(--white);background:linear-gradient(160deg,#e8d2c4,#a77b62)}

/* Projects */
.projects .section-title{top:2847px}
.project{position:absolute;width:311px;height:292px}
.view-btn{left:523px;top:3559px;width:153px;height:42px}

/* Contact */
.contact{position:absolute;left:0;top:3688px;width:1200px;height:456px;background:linear-gradient(180deg,#eef3ea 0%,#e3ecdd 100%)}
.contact-art{left:0;top:3770px;width:600px;height:374px;background:linear-gradient(180deg,#eef3ea 0%,#b8cbd9 55%,#3d68ad 85%,#5f9a3a 100%)}
.field{position:absolute;background:var(--white);border:1px solid #c7c7c7;border-radius:22px;font-size:14px;color:#444;padding:11px 20px}
.send-btn{left:608px;top:4044px;width:153px;height:42px}

/* Blog */
.blog .section-title{top:4216px}
.post{position:absolute;top:4293px;width:315px}
.post-img{height:193px;position:relative}
.date{position:absolute;left:8px;top:0;width:36px;height:44px;background:var(--red);color:var(--white);font-size:10px;text-align:center;line-height:13px;padding-top:8px}
.post h3{font-size:18px;font-weight:700;line-height:26px;margin-top:16px}
.post p{font-size:12.5px;line-height:26px;color:var(--grey);margin-top:10px}
.post .more{display:block;margin-top:12px;color:var(--red);font-size:14px;font-weight:700}

/* Partners */
.partners .section-title{top:4740px}
.partner{position:absolute;width:110px;height:40px;border-radius:6px;background:#d4d4d4}

/* Footer */
.footer{position:absolute;left:0;top:5030px;width:1200px;height:313px;background:var(--footer);color:var(--white)}
.footer .brand{left:110px;top:100px;color:var(--white);font-size:30px}
.social{position:absolute;left:114px;top:198px;display:flex;gap:8px}
.social span{width:30px;height:30px;border-radius:50%;background:var(--white)}
.fcol{position:absolute;top:54px}
.fcol h6{font-size:16px;font-weight:700;text-transform:uppercase;margin-bottom:18px}
.fcol li{list-style:none;font-size:13px;line-height:28px}
.fcontact li{display:flex;align-items:flex-start;gap:12px;margin-bottom:18px;font-size:13px;line-height:22px}
.fcontact .ci{flex:none;width:26px;height:26px;border-radius:50%;background:#2a2a2a;display:flex;align-items:center;justify-content:center}
.fabout p{font-size:12px;line-height:27px;width:255px}
.legal{position:absolute;top:282px;font-size:12.5px}
</style>
</head>
<body>

<!-- Hero -->
<header class="hero">
  <div class="abs" role="img" aria-label="Wind turbines and rows of solar panels beneath mountains" style="left:0;top:0;width:1200px;height:616px"></div>
  <div class="brand"><span class="dot"></span>NextRidge Power</div>
  <nav class="nav">
    <span class="active">Home</span><span>Solar Panels ⌄</span><span>About</span><span>Contact</span>
  </nav>
  <span class="btn quote-btn">Get a Quote</span>
  <h1>NEXTRIDGE POWER</h1>
  <p>Solar ownership and leases with a 25yr warranty,<br>backed by over 20yrs of combined solar experience</p>
  <span class="btn hero-btn">Get Started</span>
  <svg class="arrow" style="left:62px" viewBox="0 0 18 34"><path d="M15 2 3 17l12 15" fill="none" stroke="#fff" stroke-width="2"/></svg>
  <svg class="arrow" style="left:1110px" viewBox="0 0 18 34"><path d="M3 2l12 15L3 32" fill="none" stroke="#fff" stroke-width="2"/></svg>
  <div class="dots" style="left:562px;top:557px"><span></span><span></span><span></span><span></span></div>
</header>

<!-- About -->
<section class="about">
  <div class="abs about-frame"></div>
  <div class="abs about-photo" role="img" aria-label="Installer in a hard hat fitting rooftop solar panels"></div>
  <h2>ABOUT US</h2>
  <p class="body-text">Lorem ipsum dolor sit amet, consectetur adig elit, sed do eiusmod tempor incididunt ut labore et dolore magna aliqua. Quis ipsum suspendisse ultrices gravida. Risus com aecenas accn lacus vel facilisis. Lorem ipsum dolor sit amet, consecttur adig elit, sed do eiusmod tempor incididunt ut labore et dolore aliqua. Quis ipsum suspendisse ultrices gravida. Risus com aecenas accumsan lacus vel facilisis.</p>
  <span class="btn about-btn">Learn More</span>
</section>

<!-- Spectrum -->
<section class="spectrum" role="img" aria-label="Red tinted background of a worker installing solar panels">
  <h2 class="section-title">We Cover the Whole Spectrum</h2>
  <div class="service" style="left:120px">
    <svg width="70" height="70" viewBox="0 0 70 70" fill="none" stroke="#fff" stroke-width="2"><circle cx="35" cy="18" r="8"/><rect x="14" y="32" width="42" height="18"/><path d="M35 50v14M24 64h22"/></svg>
    <h3>SOLAR SYSTEM</h3>
    <p>Lorem ipsum dolor sit amet, tetur adipiscing elit, sed do eiusmod tempor iidunt ut labore et dolore magnua. Quis ipsum suspendisse ultrices grav Risus commodo</p>
  </div>
  <div class="service" style="left:450px">
    <svg width="70" height="70" viewBox="0 0 70 70" fill="none" stroke="#fff" stroke-width="2"><circle cx="35" cy="26" r="9"/><path d="M8 52h20l10 6h22M8 44h14l12 6"/></svg>
    <h3>ALTERNATIVE ENERGY</h3>
    <p>Lorem ipsum dolor sit amet, tetur adipiscing elit, sed do eiusmod tempor iidunt ut labore et dolore magnua. Quis ipsum suspendisse ultrices grav Risus commodo</p>
  </div>
  <div class="service" style="left:780px">
    <svg width="70" height="70" viewBox="0 0 70 70" fill="none" stroke="#fff" stroke-width="2"><circle cx="52" cy="16" r="7"/><path d="M8 20h30l-6 16H2zM6 46h56M14 46v16M34 46v16M54 46v16"/></svg>
    <h3>SOLAR PA SYSTEM</h3>
    <p>Lorem ipsum dolor sit amet, tetur adipiscing elit, sed do eiusmod tempor iidunt ut labore et dolore magnua. Quis ipsum suspendisse ultrices grav Risus commodo</p>
  </div>
</section>

<!-- Why choose us -->
<section class="why">
  <h2 class="section-title">Why Choose Us NextRidge Power</h2>

  <div class="abs why-art" role="img" aria-label="Solar panel between green leaves with two wind turbines"></div>

  <div class="icon-circle" style="left:53px;top:1859px"><svg width="30" height="30" viewBox="0 0 30 30" fill="none" stroke="#fff" stroke-width="2"><circle cx="15" cy="12" r="7"/><path d="M11 22h8M12 26h6"/></svg></div>
  <div class="feature" style="left:136px;top:1862px"><h4>Long Time to Use</h4><p>Lorem ipsum dolor samet, consectetur adipiscing elit, sed do eiusmod</p></div>

  <div class="icon-circle" style="left:53px;top:1994px"><svg width="30" height="30" viewBox="0 0 30 30" fill="none" stroke="#fff" stroke-width="2"><path d="M17 3 8 17h7l-2 10 9-14h-7z"/></svg></div>
  <div class="feature" style="left:136px;top:1997px"><h4>Always Clean Energy</h4><p>Lorem ipsum dolor samet, consectetur adipiscing elit, sed do eiusmod</p></div>

  <div class="icon-circle" style="left:53px;top:2129px"><svg width="30" height="30" viewBox="0 0 30 30" fill="none" stroke="#fff" stroke-width="2"><circle cx="15" cy="15" r="11"/><path d="M16 8l-5 8h5l-2 6"/></svg></div>
  <div class="feature" style="left:136px;top:2132px"><h4>Energy Can Be Reused</h4><p>Lorem ipsum dolor samet, consectetur adipiscing elit, sed do eiusmod</p></div>

  <div class="feature right" style="left:797px;top:1853px"><h4>Used for Many Purposes</h4><p>Lorem ipsum dolor samet, consectetur adipiscing elit, sed do eiusmod</p></div>
  <div class="icon-circle" style="left:1077px;top:1856px"><svg width="30" height="30" viewBox="0 0 30 30" fill="none" stroke="#fff" stroke-width="2"><rect x="4" y="9" width="20" height="12" rx="2"/><path d="M24 13h3v4h-3M15 10l-3 5h5l-3 5"/></svg></div>

  <div class="feature right" style="left:797px;top:1988px"><h4>Low Installation Costs</h4><p>Lorem ipsum dolor samet, consectetur adipiscing elit, sed do eiusmod</p></div>
  <div class="icon-circle" style="left:1077px;top:1991px"><svg width="30" height="30" viewBox="0 0 30 30" fill="none" stroke="#fff" stroke-width="2"><circle cx="15" cy="15" r="11"/><path d="M15 8v14M18 11h-4a2 2 0 0 0 0 4h2a2 2 0 0 1 0 4h-4"/></svg></div>

  <div class="feature right" style="left:797px;top:2123px"><h4>Easy Installation</h4><p>Lorem ipsum dolor samet, consectetur adipiscing elit, sed do eiusmod</p></div>
  <div class="icon-circle" style="left:1077px;top:2126px"><svg width="30" height="30" viewBox="0 0 30 30" fill="none" stroke="#fff" stroke-width="2"><rect x="5" y="5" width="20" height="13"/><path d="M5 11h20M15 5v13M15 18v7M10 25h10"/></svg></div>
</section>

<!-- Testimonials -->
<section class="testimonials">
  <h2 class="section-title">Testimonials</h2>
  <svg class="arrow" style="left:70px;top:186px" viewBox="0 0 18 34"><path d="M15 2 3 17l12 15" fill="none" stroke="#fff" stroke-width="2"/></svg>
  <div class="avatar" style="left:118px" role="img" aria-label="Customer portrait"></div>
  <div class="quote" style="left:199px">
    <p>"Sed ut perspiciatis unde omnis iste nat sit voluptatem accusantium doloremque laudtium, m rem aperiam, eaque ipsa quae ab illo inventore veritatis et quasi architecto beatae vitae dicta sunt explicabo"</p>
    <h5>Marcus T.</h5><small>Lorem ipsum dolor</small>
  </div>
  <div class="avatar" style="left:616px" role="img" aria-label="Customer portrait"></div>
  <div class="quote" style="left:695px">
    <p>"Sed ut perspiciatis unde omnis iste nat sit voluptatem accusantium doloremque laudtium, m rem aperiam, eaque ipsa quae ab illo inventore veritatis et quasi architecto beatae vitae dicta sunt explicabo"</p>
    <h5>Lena R.</h5><small>Lorem ipsum dolor</small>
  </div>
  <svg class="arrow" style="left:1104px;top:186px" viewBox="0 0 18 34"><path d="M3 2l12 15L3 32" fill="none" stroke="#fff" stroke-width="2"/></svg>
  <div class="dots grey" style="left:563px;top:377px"><span></span><span></span><span></span><span></span></div>
</section>

<!-- Projects -->
<section class="projects">
  <h2 class="section-title">Our Incredible Projects</h2>
  <div class="project" style="left:110px;top:2920px;background:linear-gradient(180deg,#5d8fd0,#2d4f8c 70%,#7a4a34)" role="img" aria-label="Installer on a roof ladder beside solar panels"></div>
  <div class="project" style="left:444px;top:2920px;background:linear-gradient(180deg,#d9c6a8,#7fa3c9 45%,#2a4b84)" role="img" aria-label="City towers behind a solar panel array"></div>
  <div class="project" style="left:776px;top:2920px;background:linear-gradient(180deg,#2d4fa6,#5577c0 50%,#b9b9c0)" role="img" aria-label="House roof with solar panels and a ladder"></div>
  <div class="project" style="left:110px;top:3233px;background:linear-gradient(180deg,#9ab4c9,#4a4f5a 55%,#2d3f66)" role="img" aria-label="Tiled roof fitted with solar panels"></div>
  <div class="project" style="left:444px;top:3233px;background:linear-gradient(160deg,#d9dee6,#9fb2c8 45%,#8a3d2d)" role="img" aria-label="Two installers fitting a panel near a ladder"></div>
  <div class="project" style="left:776px;top:3233px;background:linear-gradient(180deg,#cfdbe9,#5c7fb5 50%,#2b4479)" role="img" aria-label="Worker in a safety vest installing panels"></div>
  <span class="btn view-btn">View All</span>
</section>

<!-- Contact -->
<section class="contact"></section>
<div class="abs contact-art" role="img" aria-label="Illustrated city skyline with wind turbines and solar panels"></div>
<h2 class="abs" style="left:610px;top:3737px;font-size:36px;font-weight:700">CONTACT US</h2>
<div class="field" style="left:601px;top:3808px;width:245px;height:42px">Name</div>
<div class="field" style="left:861px;top:3808px;width:246px;height:42px">Phone</div>
<div class="field" style="left:601px;top:3864px;width:512px;height:42px">Email</div>
<div class="field" style="left:601px;top:3920px;width:512px;height:101px">Message</div>
<span class="btn send-btn">Send</span>

<!-- Blog -->
<section class="blog">
  <h2 class="section-title">Latest Blog</h2>
  <article class="post" style="left:110px">
    <div class="post-img" style="background:linear-gradient(180deg,#6d95cf,#274785)" role="img" aria-label="Rooftop solar panels being installed"><span class="date">Jan<br>10</span></div>
    <h3>The standard Lorem Ipsum Sed passage</h3>
    <p>Lorem ipsum dolor sit amet, consectetur adipiscing elit, sed do eiusmod tempor incididunt ut labore et dolore magna aliqua.</p>
    <span class="more">LEARN MORE ⟶</span>
  </article>
  <article class="post" style="left:442px">
    <div class="post-img" style="background:linear-gradient(180deg,#5c8d46,#3c4a5e 60%,#c7cdd6)" role="img" aria-label="Hand holding a solar power bank"><span class="date">Feb<br>11</span></div>
    <h3>The standard Lorem Ipsum Sed passage</h3>
    <p>Lorem ipsum dolor sit amet, consectetur adipiscing elit, sed do eiusmod tempor incididunt ut labore et dolore magna aliqua.</p>
    <span class="more">LEARN MORE ⟶</span>
  </article>
  <article class="post" style="left:774px">
    <div class="post-img" style="background:linear-gradient(180deg,#e8edf2,#9aa7b6 50%,#6c8a4a)" role="img" aria-label="Ground mounted solar panel on a field"><span class="date">Jan<br>10</span></div>
    <h3>The standard Lorem Ipsum Sed passage</h3>
    <p>Lorem ipsum dolor sit amet, consectetur adipiscing elit, sed do eiusmod tempor incididunt ut labore et dolore magna aliqua.</p>
    <span class="more">LEARN MORE ⟶</span>
  </article>
</section>

<!-- Partners -->
<section class="partners">
  <h2 class="section-title">Our Partners</h2>
  <div class="partner" style="left:109px;top:4819px"></div>
  <div class="partner" style="left:339px;top:4819px"></div>
  <div class="partner" style="left:546px;top:4819px"></div>
  <div class="partner" style="left:750px;top:4819px"></div>
  <div class="partner" style="left:984px;top:4819px;width:60px;border-radius:50%"></div>
  <div class="partner" style="left:109px;top:4918px"></div>
  <div class="partner" style="left:339px;top:4918px"></div>
  <div class="partner" style="left:546px;top:4918px"></div>
  <div class="partner" style="left:780px;top:4913px;width:50px;height:50px"></div>
  <div class="partner" style="left:959px;top:4918px"></div>
</section>

<!-- Footer -->
<footer class="footer">
  <div class="brand"><span class="dot"></span>NextRidge Power</div>
  <div class="social"><span></span><span></span><span></span><span></span></div>
  <div class="fcol" style="left:373px">
    <h6>Quick Links</h6>
    <ul><li>Home</li><li>Solar panels</li><li>About</li><li>Blog</li><li>Contact</li></ul>
  </div>
  <div class="fcol fcontact" style="left:577px">
    <h6>Contact Us</h6>
    <ul>
      <li><span class="ci"><svg width="12" height="14" viewBox="0 0 12 14"><path d="M6 0a5 5 0 0 1 5 5c0 4-5 9-5 9S1 9 1 5a5 5 0 0 1 5-5z" fill="#fff"/><circle cx="6" cy="5" r="2" fill="#2a2a2a"/></svg></span>48 Ridgeline Ave, Summit City<br>10150, United States</li>
      <li><span class="ci"><svg width="12" height="12" viewBox="0 0 12 12"><path d="M2 1l2.5-.5L6 4 4.5 5.5a7 7 0 0 0 2 2L8 6l3.5 1.5L11 10c-5 1-10-4-9-9z" fill="#fff"/></svg></span>555 014 2290</li>
      <li><span class="ci"><svg width="13" height="10" viewBox="0 0 13 10"><rect x=".5" y=".5" width="12" height="9" fill="none" stroke="#fff"/><path d="M.5.5l6 5 6-5" fill="none" stroke="#fff"/></svg></span>info@nextridgepower.com</li>
    </ul>
  </div>
  <div class="fcol fabout" style="left:840px">
    <h6>About Us</h6>
    <p>Lorem ipsum dolor sit consectetur adipiscing elit, sed do eiusmod tpor incididunt ut labore et dolore magnliqua. Quis ipsum suspendisse ultrices gravRisus commodo viverra maecenas accumsan lacus vel facilisis.</p>
  </div>
  <span class="legal" style="left:110px">Copyright © 2021. NextRidge Power All Rights Reserved</span>
  <span class="legal" style="left:846px">Terms and Conditions &nbsp;|&nbsp; Privacy Policy</span>
</footer>

</body>
</html>
```